LinkedIn Cover Image

We need a Linked In Cover Image for our Linked In Business Page.

The dimensions needed are: 1536 x 768px.

Here's a link to our website: www.bramwellrenewal.com
LinkedIn Profile: https://www.profilehub.example/company/bramwell-renewal-services/

Font styles to use
Sans Serif

Colors

Designer to choose colors to be used in the design.

```html
<!DOCTYPE html>
<html lang="en">
<head>
<meta charset="utf-8">
<title>Bramwell Renewal Services – Cover Banner Concepts</title>
<link href="https://fonts.googleapis.com/css2?family=Open+Sans:wght@400;600;700&family=Oswald:wght@500;700&family=Lilita+One&display=swap" rel="stylesheet">
<style>
:root{
  --orange:#f28a1a;
  --orange-deep:#e06a0a;
  --orange-light:#f7b23a;
  --yellow:#ffd21c;
  --gold-dark:#7a5208;
  --cream:#fdf1dc;
  --grey:#bdb6aa;
  --grey-light:#e6e2da;
  --charcoal:#2b2b2b;
  --white:#ffffff;
  --green:#8ccc1e;
  --green-dark:#0f5a1e;
  --sans:'Open Sans',Arial,sans-serif;
}
*{box-sizing:border-box;margin:0;padding:0}
html,body{width:937px;height:1200px;overflow:hidden;background:var(--white)}
.sheet{position:relative;width:937px;height:1200px}
.banner{position:absolute;left:60px;width:818px;height:204px;overflow:hidden}
.banner--one{top:58px;background:linear-gradient(90deg,var(--orange) 0%,var(--orange-light) 45%,var(--orange) 100%)}
.banner--two{top:335px;background:linear-gradient(90deg,var(--grey) 0%,var(--grey-light) 45%,var(--grey) 100%)}
.banner--three{top:614px;background:radial-gradient(circle at 52% 45%,var(--yellow) 0%,var(--orange-light) 35%,var(--orange) 75%)}
.banner--four{top:898px;background:linear-gradient(90deg,var(--orange-light) 0%,var(--yellow) 55%,var(--orange) 100%)}
.abs{position:absolute}
.brand{position:absolute;font-family:var(--sans);font-weight:700;color:var(--white);line-height:1.05;text-transform:uppercase;letter-spacing:.5px}
.tagline{position:absolute;font-family:var(--sans);font-weight:600;color:var(--white);letter-spacing:1.5px;text-transform:uppercase;white-space:nowrap}
.service{position:absolute;width:100px;margin-left:-50px;text-align:center;font-family:var(--sans);color:var(--white);text-transform:uppercase;line-height:1.15;white-space:nowrap}
.service svg{display:block;margin:0 auto 2px}
.service--compact{width:76px;margin-left:-38px}
.label{position:absolute;width:100px;margin-left:-50px;text-align:center;font-family:var(--sans);color:var(--white);text-transform:uppercase;line-height:1.2;white-space:nowrap}
.photo{position:absolute}
</style>
</head>
<body>
<svg width="0" height="0" style="position:absolute" aria-hidden="true">
  <defs>
    <symbol id="ic-fire" viewBox="0 0 40 40"><circle cx="20" cy="20" r="18" fill="#fff" stroke="#e06a0a" stroke-width="2"/><path fill="#f28a1a" d="M20 8C24 14 28 17 28 24a8 8 0 0 1-16 0c0-4 2-6 4-9 0 3 1 5 3 6 0-5 0-9 1-13z"/></symbol>
    <symbol id="ic-mold" viewBox="0 0 40 40"><circle cx="20" cy="20" r="18" fill="#fff" stroke="#e06a0a" stroke-width="2"/><path fill="#f28a1a" d="M12 14q8-7 16 0v9q-8 7-16 0z"/><circle cx="14" cy="27" r="4.5" fill="#f28a1a"/><circle cx="26" cy="27" r="4.5" fill="#f28a1a"/><rect x="16" y="16" width="8" height="4" rx="2" fill="#fff"/></symbol>
    <symbol id="ic-water" viewBox="0 0 40 40"><circle cx="20" cy="20" r="18" fill="#fff" stroke="#e06a0a" stroke-width="2"/><path fill="#f28a1a" d="M20 8C24 15 28 19 28 25a8 8 0 0 1-16 0c0-6 4-10 8-17z"/></symbol>
    <symbol id="ic-star" viewBox="0 0 40 40"><circle cx="20" cy="20" r="18" fill="#fff" stroke="#e06a0a" stroke-width="2"/><polygon fill="#f4d9b8" stroke="#e06a0a" stroke-width="1" points="20,9 22.7,16.3 30.5,16.6 24.4,21.4 26.5,28.9 20,24.6 13.5,28.9 15.6,21.4 9.5,16.6 17.3,16.3"/></symbol>
  </defs>
</svg>

<main class="sheet">

  <section class="banner banner--one">
    <div class="brand" style="left:114px;top:12px;font-size:38px;color:var(--orange-deep);letter-spacing:1px">Bramwell<br><span style="font-size:15px;color:var(--charcoal)">Renewal Services</span></div>
    <div class="tagline" style="left:114px;top:86px;font-size:11px">Getting you back to normal</div>
    <div class="service" style="left:77px;top:110px;font-size:11px"><svg width="46" height="46"><use href="#ic-fire"/></svg>Fire and smoke<br>restoration</div>
    <div class="service" style="left:174px;top:110px;font-size:11px"><svg width="46" height="46"><use href="#ic-mold"/></svg>Mold<br>restoration</div>
    <div class="service" style="left:280px;top:110px;font-size:11px"><svg width="46" height="46"><use href="#ic-water"/></svg>Water and flood<br>restoration</div>
    <div class="service" style="left:385px;top:110px;font-size:11px"><svg width="46" height="46"><use href="#ic-star"/></svg>Specialty<br>services</div>
    <div class="photo" role="img" aria-label="Stacked photos of building interiors under restoration" style="left:568px;top:6px;width:220px;height:198px;background:linear-gradient(180deg,#dcdcd8 0%,#a89a88 45%,#3a3432 100%)"></div>
    <div class="photo" role="img" aria-label="Ceiling ductwork during restoration" style="left:495px;top:96px;width:170px;height:108px;background:linear-gradient(160deg,#5a5252 0%,#2a2424 100%)"></div>
  </section>

  <section class="banner banner--two">
    <svg class="abs" width="818" height="204" style="left:0;top:0" aria-hidden="true">
      <path d="M0 0H818V56H460L420 72H150L125 56H0Z" fill="#ef7d12"/>
      <path d="M125 56L150 72H420L460 56H300L262 66H150Z" fill="#222"/>
    </svg>
    <div class="tagline" style="right:30px;top:16px;font-size:21px;letter-spacing:2px">Getting you back to normal</div>
    <div class="brand" style="left:46px;top:98px;font-size:36px;color:var(--orange-deep)">Bramwell<br><span style="font-size:15px;color:var(--charcoal)">Renewal Services</span></div>
    <svg class="abs" width="818" height="204" style="left:0;top:0" aria-hidden="true">
      <g fill="#e8780e">
        <polygon points="448,84 481,103 481,141 448,160 415,141 415,103"/>
        <polygon points="547,84 580,103 580,141 547,160 514,141 514,103"/>
        <polygon points="652,84 685,103 685,141 652,160 619,141 619,103"/>
        <polygon points="757,84 790,103 790,141 757,160 724,141 724,103"/>
      </g>
      <use href="#ic-fire" x="428" y="102" width="40" height="40"/>
      <use href="#ic-mold" x="527" y="102" width="40" height="40"/>
      <use href="#ic-water" x="632" y="102" width="40" height="40"/>
      <use href="#ic-star" x="737" y="102" width="40" height="40"/>
    </svg>
    <div class="label" style="left:448px;top:172px;font-size:8px">Fire and smoke<br>restoration</div>
    <div class="label" style="left:547px;top:172px;font-size:8px">Mold<br>restoration</div>
    <div class="label" style="left:652px;top:172px;font-size:8px">Water and flood<br>restoration</div>
    <div class="label" style="left:757px;top:172px;font-size:8px">Specialty<br>services</div>
  </section>

  <section class="banner banner--three">
    <div class="photo" role="img" aria-label="Pale city skyline silhouette" style="left:80px;top:130px;width:640px;height:74px;background:linear-gradient(180deg,rgba(253,241,220,.6),rgba(253,241,220,.9))"></div>
    <div class="abs" style="left:108px;top:46px;transform:rotate(-8deg);transform-origin:left top;font-family:'Lilita One',sans-serif;line-height:.9;white-space:nowrap">
      <div style="font-size:32px;color:var(--cream)">GETTING YOU</div>
      <div style="font-size:66px;color:var(--green);margin-left:4px">BACK</div>
      <div style="font-size:34px;color:var(--green-dark);margin-left:8px">TO NORMAL</div>
    </div>
    <div class="photo" role="img" aria-label="Cartoon knight mascot holding a squeegee" style="left:400px;top:40px;width:184px;height:164px;border-radius:40% 40% 0 0;background:linear-gradient(180deg,#5b8fe0 0%,#1f3f9a 100%)"></div>
    <div class="abs" style="left:456px;top:2px;width:130px;height:100px;border-radius:50%;background:var(--white)"></div>
    <div class="brand" style="left:468px;top:36px;font-size:19px;color:var(--orange-deep)">Bramwell<br><span style="font-size:8px">Renewal Services</span></div>
    <div class="service service--compact" style="left:710px;top:28px;font-size:9px"><svg width="34" height="34"><use href="#ic-fire"/></svg>Fire and smoke<br>restoration</div>
    <div class="service service--compact" style="left:784px;top:28px;font-size:9px"><svg width="34" height="34"><use href="#ic-mold"/></svg>Mold<br>restoration</div>
    <div class="service service--compact" style="left:706px;top:104px;font-size:9px"><svg width="34" height="34"><use href="#ic-water"/></svg>Water and flood<br>restoration</div>
    <div class="service service--compact" style="left:784px;top:104px;font-size:9px"><svg width="34" height="34"><use href="#ic-star"/></svg>Specialty<br>services</div>
  </section>

  <section class="banner banner--four">
    <div class="photo" role="img" aria-label="Hexagon collage of restored office interiors" style="left:0;top:0;width:330px;height:204px;background:linear-gradient(90deg,#2e2826 0%,#cfd0cc 45%,#6a5a48 100%)"></div>
    <svg class="abs" width="818" height="204" style="left:0;top:0" aria-hidden="true">
      <polygon points="300,2 368,2 408,100 368,200 300,200 240,100" fill="#8a5f0c" opacity=".95"/>
      <polygon points="488,30 560,30 600,102 560,174 488,174 448,102" fill="#ffffff" opacity=".08"/>
    </svg>
    <div class="brand" style="left:250px;top:76px;font-size:26px;color:var(--orange-light)">Bramwell<br><span style="font-size:10px;color:var(--white)">Renewal Services</span></div>
    <div class="abs" style="left:434px;top:78px;font-family:'Oswald',sans-serif;font-weight:700;color:var(--white);line-height:.95;text-transform:uppercase;white-space:nowrap">
      <div style="font-size:26px">Getting you</div>
      <div style="font-size:20px">Back to normal</div>
    </div>
    <div class="service" style="left:672px;top:30px;font-size:10px;width:84px;margin-left:-42px"><svg width="38" height="38"><use href="#ic-fire"/></svg>Fire and smoke<br>restoration</div>
    <div class="service" style="left:756px;top:30px;font-size:10px;width:80px;margin-left:-40px"><svg width="38" height="38"><use href="#ic-mold"/></svg>Mold<br>restoration</div>
    <div class="service" style="left:671px;top:114px;font-size:10px;width:84px;margin-left:-42px"><svg width="38" height="38"><use href="#ic-water"/></svg>Water and flood<br>restoration</div>
    <div class="service" style="left:756px;top:114px;font-size:10px;width:80px;margin-left:-40px"><svg width="38" height="38"><use href="#ic-star"/></svg>Specialty<br>services</div>
  </section>

</main>
</body>
</html>
```